The Wellness Barn Business Card

Info for the front..... (in whichever order and layout looks best)
Carla Penhallow
Physiotherapist
4/37 Upper Creekbank Rd
Tallowbrook
QLD 4712
0462305178
carlapenhallow57@mailbox.example
www.thewellnessbarn.example.au
on the back I would like to be able to write appointments so probably just that heading with lines.
I like a sort of rustic style but mostly professional, colours in naturals, beige, brown, green etc. I dont mind if the logo colour is changed slightly to suit.

```html
<!DOCTYPE html>
<html lang="en">
<head>
<meta charset="utf-8">
<title>The Wellness Barn – Business Card</title>
<link href="https://fonts.googleapis.com/css2?family=Source+Sans+3:wght@300;400;600;700&display=swap" rel="stylesheet">
<style>
  :root {
    --forest: #2d4620;
    --ink: #2f4524;
    --paper: #ffffff;
    --backdrop-top: #f7f7f7;
    --backdrop-bottom: #d2d2d2;
    --edge: #1f2a18;
  }
  * { margin: 0; padding: 0; box-sizing: border-box; }
  html, body { width: 1163px; height: 1200px; overflow: hidden; }
  body {
    position: relative;
    background: radial-gradient(ellipse at 40% 10%, var(--backdrop-top) 0%, var(--backdrop-bottom) 100%);
    font-family: "Source Sans 3", "Source Sans Pro", sans-serif;
    color: var(--ink);
  }
  .card {
    position: absolute;
    width: 614px;
    height: 374px;
    background: var(--paper);
    border: 1px solid var(--edge);
    overflow: hidden;
  }
  .card--front { left: 275px; top: 218px; }
  .card--back { left: 272px; top: 636px; }

  /* front */
  .front-arc { position: absolute; inset: 0; width: 100%; height: 100%; }
  .brand-name {
    position: absolute;
    left: 0; right: 0;
    text-align: center;
    font-weight: 700;
    color: var(--paper);
  }
  .card--front .brand-name { top: 40px; font-size: 38px; line-height: 1; }
  .role {
    position: absolute; left: 0; right: 0; top: 178px;
    text-align: center; font-weight: 300; font-size: 27px; letter-spacing: 0.3px;
  }
  .person {
    position: absolute; left: 0; right: 0; top: 212px;
    text-align: center; font-weight: 700; font-size: 31px; letter-spacing: 0.5px;
  }
  .contact-row {
    position: absolute; left: 0; right: 0; top: 258px;
    display: flex; justify-content: center; align-items: center; gap: 16px;
    font-size: 20px;
  }
  .contact-item { display: flex; align-items: center; gap: 8px; }
  .contact-icon { width: 26px; height: 26px; flex: none; }
  .website {
    position: absolute; left: 0; right: 0; top: 297px;
    text-align: center; font-weight: 700; font-size: 24px; letter-spacing: 0.2px;
  }
  .address {
    position: absolute; left: 0; right: 0;
    text-align: center; font-size: 17px; letter-spacing: 1.6px;
  }
  .card--front .address { top: 343px; }

  /* back */
  .header-band {
    position: absolute; left: 0; top: 0; width: 100%; height: 66px;
    background: var(--forest);
  }
  .card--back .brand-name {
    left: 32px; right: auto; top: 9px; width: 140px;
    text-align: left; font-size: 21px; line-height: 1.15;
  }
  .header-title {
    position: absolute; right: 26px; top: 19px;
    color: var(--paper); font-size: 23px;
  }
  .header-title .role-label { font-weight: 300; }
  .header-title .name-label { font-weight: 700; }
  .write-line {
    position: absolute; right: 25px; height: 1.5px; background: var(--ink);
  }
  .footer-band {
    position: absolute; left: 0; bottom: 0; width: 100%; height: 43px;
    background: var(--forest);
  }
  .card--back .address { bottom: 11px; color: var(--paper); }
</style>
</head>
<body>

<section class="card card--front" aria-label="Business card front">
  <svg class="front-arc" viewBox="0 0 614 374" preserveAspectRatio="none" aria-hidden="true">
    <rect width="614" height="374" fill="var(--forest)"/>
    <path d="M0 187 Q307 10 614 187 L614 374 L0 374 Z" fill="none" stroke="#ffffff" stroke-width="2" transform="translate(0,-4)"/>
    <path d="M0 187 Q307 10 614 187 L614 374 L0 374 Z" fill="#ffffff"/>
  </svg>
  <div class="brand-name">The Wellness Barn</div>
  <div class="role">PHYSIOTHERAPIST</div>
  <div class="person">CARLA PENHALLOW</div>
  <div class="contact-row">
    <span class="contact-item">
      <svg class="contact-icon" viewBox="0 0 26 26" aria-hidden="true">
        <circle cx="13" cy="13" r="11.5" fill="none" stroke="var(--ink)" stroke-width="2"/>
        <path d="M9 7.5 l2.2 0 l1 3 l-1.6 1.3 q1.3 2.7 4 4 l1.3 -1.6 l3 1 l0 2.2 q-0.5 1.3 -2 1.3 q-5.5 -0.5 -9 -6 q-1 -2 -0.3 -3.9 q0.5 -1.3 1.4 -1.3 z" fill="var(--ink)"/>
      </svg>
      0462305178
    </span>
    <span class="contact-item">
      <svg class="contact-icon" viewBox="0 0 26 26" aria-hidden="true">
        <circle cx="13" cy="13" r="11.5" fill="none" stroke="var(--ink)" stroke-width="2"/>
        <rect x="7" y="9" width="12" height="8.5" fill="none" stroke="var(--ink)" stroke-width="1.6"/>
        <path d="M7 9 L13 14 L19 9" fill="none" stroke="var(--ink)" stroke-width="1.6"/>
      </svg>
      carlapenhallow57@mailbox.example
    </span>
  </div>
  <div class="website">WWW.THEWELLNESSBARN.EXAMPLE.AU</div>
  <div class="address">4/37 UPPER CREEKBANK RD TALLOWBROOK QLD 4712</div>
</section>

<section class="card card--back" aria-label="Business card back, appointment lines">
  <div class="header-band"></div>
  <div class="brand-name">The Wellness Barn</div>
  <div class="header-title"><span class="role-label">PHYSIOTHERAPIST</span> <span class="name-label">CARLA PENHALLOW</span></div>
  <div class="write-line" style="top:112px; left:190px;"></div>
  <div class="write-line" style="top:152px; left:33px;"></div>
  <div class="write-line" style="top:193px; left:33px;"></div>
  <div class="write-line" style="top:233px; left:33px;"></div>
  <div class="write-line" style="top:273px; left:33px;"></div>
  <div class="write-line" style="top:319px; left:33px;"></div>
  <div class="footer-band"></div>
  <div class="address">4/37 UPPER CREEKBANK RD TALLOWBROOK QLD 4712</div>
</section>

</body>
</html>
```